Design a menu for health restaurant

A health food restaurant in Los Angeles is seeking menu design. Our foods are made from scratch using whole ingredients.
Name: Grubb Larder
Address: 1000 E 60th StLos Angeles, CA 90247
Website: www.GrubbLarder.example
We are looking for a clean and simple menu. Brand colors are white/tan, green and orange.

Please see attached excel with menu items and logo. We do not yet have prices.

Colors
f78f20
9bcb3c
ffffff
fff3d1

Requirements
Must have
• Easy to read.
Trifold menu design (front and back).
VEGAN, VEGETARIAN, GLUTEN FREE, CONTAINS NUTS symbols.
Logo.
Nice to have
• Incorporate brand colors, but still be easy to read.
We would like to use the Belco font (attached) if it works. If not we are open to a similar font that is easy to read.

Please see attached images.
We like the images and headers of OPTION 1. Would like something similar in trifold format.
We like the clean fonts of OPTION 2.

```html
<!DOCTYPE html>
<html lang="en">
<head>
<meta charset="utf-8">
<title>Grubb Larder Menu</title>
<link rel="stylesheet" href="https://fonts.googleapis.com/css2?family=Didact+Gothic&display=swap">
<style>
:root{
  --orange:#f78f20;
  --green:#9bcb3c;
  --tan:#fff3d1;
  --white:#ffffff;
  --ink:#4a4a4a;
  --drink-title:#7a3b12;
  --nut:#7b4a22;
  --sprout:#f5c518;
  --deep-green:#2e8b3e;
}
*{box-sizing:border-box;margin:0;padding:0}
html,body{width:1200px;height:927px;overflow:hidden;background:var(--white)}
body{font-family:"Didact Gothic",sans-serif;color:var(--ink);position:relative}
.panel{position:absolute;overflow:hidden}
.section-title{font-size:28px;font-weight:400;color:var(--orange);letter-spacing:.5px;line-height:32px;text-transform:uppercase}
.item-name{font-size:16px;color:var(--green);letter-spacing:1.4px;line-height:18px;white-space:nowrap}
.item-name .price{font-size:13px;letter-spacing:.3px}
.item-desc{font-size:12.6px;line-height:15.2px;letter-spacing:.35px}
.tag{display:inline-block;width:13px;height:15px;vertical-align:-2px;margin-left:3px}
.photo{position:absolute}

/* burgers */
.burgers{left:0;top:0;width:401px;height:420px;padding:22px 0 0 27px}
.burgers .item{height:72.5px}
.burgers .section-title{margin-bottom:4px}

/* snacks */
.snacks{left:0;top:420px;width:260px;height:269px;background:var(--tan);padding:8px 0 0 27px}
.snacks .section-title{margin-bottom:4px}
.snacks .item{margin-bottom:5px}

/* desserts */
.desserts{left:402px;top:0;width:399px;height:275px;background:var(--tan);padding:22px 0 0 25px}
.desserts .item{height:58px}
.desserts .section-title{margin-bottom:4px}
.legend{position:absolute;left:653px;top:0;width:148px;height:130px;background:var(--white);padding:14px 0 0 13px}
.legend li{list-style:none;font-size:12.5px;height:27.3px;letter-spacing:.3px}
.legend .tag{width:18px;height:20px;margin:0 14px 0 0;vertical-align:-5px}

/* drinks */
.drinks{left:402px;top:275px;width:399px;height:414px;background:var(--orange);padding:16px 0 0 25px}
.drinks .section-title{color:var(--white);margin-bottom:7px;font-size:28px}
.drinks .item{margin-bottom:7px}
.drinks .item-name{color:var(--drink-title)}
.drinks .item-desc{color:var(--tan);font-size:12.3px;line-height:13.8px}

/* brand */
.brand{left:803px;top:0;width:397px;height:275px;display:flex;flex-direction:column;align-items:center;justify-content:center;gap:14px}
.brand-mark{width:86px;height:86px;border-radius:50%;background:var(--orange)}
.brand-name{font-size:26px;color:var(--orange);letter-spacing:3px;text-transform:uppercase}

/* combos */
.combos{left:156px;top:692px;width:243px;height:235px;background:var(--green);padding:12px 19px 0 0;text-align:right;color:var(--white)}
.combos .section-title{color:var(--white);margin-bottom:3px}
.combos .item{margin-bottom:9px}
.combos .item-name{color:var(--white)}
.combos .item-desc{font-size:12.3px;color:var(--white)}

/* bottled */
.bottled{left:554px;top:692px;width:247px;height:235px;padding:12px 22px 0 0;text-align:right}
.bottled .section-title{text-transform:none;font-size:22px;letter-spacing:2px;margin-bottom:12px}
.bottled .item{font-size:12.3px;letter-spacing:.3px;line-height:14px;margin-bottom:15px}
.bottled .flavors{color:var(--orange)}

/* story */
.story{left:803px;top:692px;width:397px;height:235px;background:var(--green);color:var(--white);text-align:center;padding:20px 0 0}
.story .pitch{font-size:17px;line-height:20.5px;letter-spacing:.6px;margin-bottom:22px}
.story .contact{font-size:14px;line-height:19.8px;color:var(--deep-green)}
</style>
</head>
<body>

<svg width="0" height="0" style="position:absolute" aria-hidden="true">
  <symbol id="icon-vegan" viewBox="0 0 20 22"><path d="M15 1C6 3 2 9 3 16c1 3 3 5 6 5 6-1 8-9 6-20z" fill="#9bcb3c"/><path d="M13 4 6 19" stroke="#fff" stroke-width="1.2"/></symbol>
  <symbol id="icon-vegetarian" viewBox="0 0 20 22"><path d="M15 1C6 3 2 9 3 16c1 3 3 5 6 5 6-1 8-9 6-20z" fill="#f78f20"/><path d="M13 4 6 19" stroke="#fff" stroke-width="1.2"/></symbol>
  <symbol id="icon-gluten" viewBox="0 0 20 22"><path d="M9 21V11M9 11C6 10 3 7 3 3c3 1 6 4 6 8zm0 0c3-1 7-4 8-9-4 1-7 4-8 9z" stroke="#f5c518" stroke-width="2.2" fill="none" stroke-linecap="round"/></symbol>
  <symbol id="icon-nut" viewBox="0 0 20 22"><ellipse cx="10" cy="11" rx="6" ry="9.5" transform="rotate(20 10 11)" fill="#7b4a22"/><path d="M13 3C8 8 12 13 7 19" stroke="#fff" stroke-width="1.1" fill="none"/></symbol>
</svg>

<section class="panel burgers">
  <h2 class="section-title">Burgers n’ Sammies</h2>
  <div class="item"><h3 class="item-name">Air Fried Chicken Sammy | <span class="price">12.34</span></h3><p class="item-desc">Air fried chicken breast topped with red leaf lettuce, tomato, house made pickles and Larder Sauce on a bun served with choice of salad of fries.</p></div>
  <div class="item"><h3 class="item-name">Grilled Chicken Sammy | <span class="price">12.34</span></h3><p class="item-desc">Grilled chicken topped with guacamole, red leaf lettuce, tomato, house made pickles and Larder Sauce. Served with regular fries or side salad.</p></div>
  <div class="item"><h3 class="item-name">Classic Beef Burger | <span class="price">12.34</span></h3><p class="item-desc">House seasoned beef burger topped with red leaf lettuce, tomato, cheddar cheese, house made pickles and Larder Sauce on a bun served with choice of salad of fries.</p></div>
  <div class="item"><h3 class="item-name">Black Bean Pine Nut Burger | <span class="price">12.34</span> <svg class="tag"><use href="#icon-vegan"/></svg><svg class="tag"><use href="#icon-nut"/></svg></h3><p class="item-desc">House made black bean pine nut burger topped with red leaf lettuce, tomato, house made pickles and mustard aioli on a bun served with choice of salad of fries.</p></div>
  <div class="item"><h3 class="item-name">Salmon Burger | <span class="price">12.34</span></h3><p class="item-desc">House made salmon burger topped with red leaf lettuce, tomato, house made pickles and Larder yogurt on a bun served with choice of salad of fries.</p></div>
</section>

<section class="panel snacks">
  <h2 class="section-title">Snacks n’ Sides</h2>
  <div class="item"><h3 class="item-name">Fries &nbsp;| <span class="price">12.34</span> <svg class="tag"><use href="#icon-vegan"/></svg><svg class="tag"><use href="#icon-gluten"/></svg></h3><p class="item-desc">Hand cut air-fries with house seasonings.<br>Choose regular or sweet potato fries.</p></div>
  <div class="item"><h3 class="item-name">Side Salad &nbsp;| <span class="price">12.34</span></h3><p class="item-desc">Your choice of House, Golden Beet, Mediterranean, or Vegan Chef side salad. (24oz)</p></div>
  <div class="item"><h3 class="item-name">Guac + Chips | <span class="price">12.34</span> <svg class="tag"><use href="#icon-vegan"/></svg><svg class="tag"><use href="#icon-gluten"/></svg></h3><p class="item-desc">Guacamole with blue corn tortilla chips.</p></div>
  <div class="item"><h3 class="item-name">Hummus + Chips | <span class="price">12.34</span> <svg class="tag"><use href="#icon-vegan"/></svg><svg class="tag"><use href="#icon-gluten"/></svg></h3><p class="item-desc">Hummus with blue corn tortilla chips.</p></div>
</section>

<div class="photo" role="img" aria-label="Guacamole in a cup with a blue corn tortilla chip" style="left:262px;top:420px;width:137px;height:269px;background:linear-gradient(160deg,#3d3540 0%,#7a7660 35%,#b9bd6a 65%,#d9dcd2 100%)"></div>

<section class="panel desserts">
  <h2 class="section-title">Desserts</h2>
  <div class="item"><h3 class="item-name">Date Coffee Cake | <span class="price">12.34</span> <svg class="tag"><use href="#icon-vegan"/></svg><svg class="tag"><use href="#icon-nut"/></svg></h3><p class="item-desc">Signature date coffee cake<br>with walnuts.</p></div>
  <div class="item"><h3 class="item-name">Fruit + Spices | <span class="price">12.34</span> <svg class="tag"><use href="#icon-vegan"/></svg><svg class="tag"><use href="#icon-gluten"/></svg></h3><p class="item-desc">Strawberry, pineapple, green apple,<br>orange, and blueberries with lime and chili seasoning.</p></div>
  <div class="item"><h3 class="item-name">Cookies | <span class="price">12.34</span> &nbsp;<svg class="tag"><use href="#icon-vegetarian"/></svg></h3><p class="item-desc">Your choice of Chocolate Chip or Double Chocolate Chip<br>fresh baked cookie.</p></div>
  <div class="item"><h3 class="item-name">Larder Chocolate Mousse | <span class="price">12.34</span> <svg class="tag"><use href="#icon-vegan"/></svg><svg class="tag"><use href="#icon-gluten"/></svg></h3><p class="item-desc">Served with grated dark chocolate.</p></div>
</section>

<ul class="legend">
  <li><svg class="tag"><use href="#icon-vegan"/></svg>Vegan</li>
  <li><svg class="tag"><use href="#icon-vegetarian"/></svg>Vegetarian</li>
  <li><svg class="tag"><use href="#icon-gluten"/></svg>Gluten Free</li>
  <li><svg class="tag"><use href="#icon-nut"/></svg>Contains Nuts</li>
</ul>

<section class="panel drinks">
  <h2 class="section-title">Drinks</h2>
  <div class="item"><h3 class="item-name">Coffee | <span class="price">12.34</span></h3><p class="item-desc">We proudly serve Tallrow Coffee, a local roaster.</p></div>
  <div class="item"><h3 class="item-name">Power Date Shake | <span class="price">12.34</span> <svg class="tag"><use href="#icon-vegan"/></svg><svg class="tag"><use href="#icon-gluten"/></svg></h3><p class="item-desc">Ice-blended energy smoothie featuring dates and coffee.</p></div>
  <div class="item"><h3 class="item-name">Heart Beet Juice | <span class="price">12.34</span> <svg class="tag"><use href="#icon-vegan"/></svg><svg class="tag"><use href="#icon-gluten"/></svg></h3><p class="item-desc">Red beet, apple, carrot, ginger, parsley, and lemon.</p></div>
  <div class="item"><h3 class="item-name">Green Leafy Juice | <span class="price">12.34</span> <svg class="tag"><use href="#icon-vegan"/></svg><svg class="tag"><use href="#icon-gluten"/></svg></h3><p class="item-desc">Spinach, kale, cucumber, apple, and oranges.</p></div>
  <div class="item"><h3 class="item-name">Orange Turmeric Juice | <span class="price">12.34</span> <svg class="tag"><use href="#icon-vegan"/></svg><svg class="tag"><use href="#icon-gluten"/></svg></h3><p class="item-desc">Turmeric, ginger, lemon, carrot, and orange topped with cracked black pepper.</p></div>
  <div class="item"><h3 class="item-name">Fireshot | <span class="price">12.34</span> <svg class="tag"><use href="#icon-vegan"/></svg><svg class="tag"><use href="#icon-gluten"/></svg></h3><p class="item-desc">Ginger and lemon shot topped with cayenne.</p></div>
  <div class="item"><h3 class="item-name">Lemonade | <span class="price">12.34</span></h3><p class="item-desc">House Made Lemonade. Choice of unsweetened or agave sweetened in Regular, Raspberry, and Lavender flavors.</p></div>
  <div class="item"><h3 class="item-name">Tea | <span class="price">12.34</span></h3><p class="item-desc">Hot or iced</p></div>
</section>

<header class="panel brand">
  <span class="brand-mark" aria-hidden="true"></span>
  <span class="brand-name">Grubb Larder</span>
</header>

<div class="photo" role="img" aria-label="Salad bowl with avocado, watermelon radish, golden beets and greens" style="left:803px;top:275px;width:397px;height:414px;background:radial-gradient(ellipse at 55% 55%,#c9b95a 0%,#8f9e55 30%,#c0487a 55%,#6f5a50 75%,#dcdcda 100%)"></div>

<div class="photo" role="img" aria-label="Salad with hummus, eggs, olives and cucumber" style="left:0;top:692px;width:153px;height:235px;background:radial-gradient(ellipse at 60% 45%,#e6d7b8 0%,#7fa04a 40%,#3e5e2c 75%,#6a4a4a 100%)"></div>

<section class="panel combos">
  <h2 class="section-title">Combos</h2>
  <div class="item"><h3 class="item-name">Soup + Salad | <span class="price">12.34</span></h3><p class="item-desc">Your choice of soup and side salad.<br>16oz soup + 38oz salad</p></div>
  <div class="item"><h3 class="item-name">Avo Toast Combo | <span class="price">12.34</span></h3><p class="item-desc">Half avocado toast and<br>your choice of soup. 16oz</p></div>
  <div class="item"><h3 class="item-name">Soup + Sammy | <span class="price">12.34</span></h3><p class="item-desc">Your choice of soup and sandwich.<br>16oz soup + Sandwich</p></div>
</section>

<div class="photo" role="img" aria-label="Raspberry lemonade in a cup with ice" style="left:402px;top:692px;width:152px;height:235px;background:linear-gradient(170deg,#f4d6da 0%,#ef8a98 35%,#e9606f 70%,#f0c7c9 100%)"></div>

<section class="panel bottled">
  <h2 class="section-title">Bottled Drinks</h2>
  <p class="item">Brightfern kombucha | 12.34<br><span class="flavors">(Harmony Trilogy, Harmony<br>Gingerberry, Harmony Mango)</span></p>
  <p class="item">Cloudmere | 12.34<br><span class="flavors">(Orange Mango, Lemon, Grapefruit)</span></p>
  <p class="item">Palmgrove Coconut Original | 12.34</p>
  <p class="item">Sparkling Water (Evermore) | 12.34</p>
  <p class="item">Still Water (Evermore) | 12.34</p>
</section>

<footer class="panel story">
  <p class="pitch">Our food is made with love:<br>love for humanity, love for flavor,<br>love for wellness,<br>and love for our customers<br>who love us back!</p>
  <p class="contact">(555) 014-2290<br>Info@GrubbLarder.example<br>2417 W 83rd St, Los Angeles, CA 90247<br>www.GrubbLarder.example</p>
</footer>

</body>
</html>
```